infographic - healing the addiction cycle

Please create a 3 slide infographic based on the three slides attached, as you can see they are builds on each other. I would love you to use pictures to complement the words and make it look beautiful. Please try to illustrate as much as possible i a looking for something really creative, clean and beautiful that articulates these concepts well.
My website is www.calmvessel.com.au so you can get an idea of branding and style.
This infographic will be used in training to teach new practitioners and clients how to heal their addictions.

Target Market(s)

Women aged 30 - 45

Industry/Entity Type

Professional Service

Font styles to use
Sans Serif

Colors

Designer to choose colors to be used in the design.

Requirements
Must have
• the blue color of my logo on it, i also like white
• Visual depictions not just words
• please look at my website to get an idea of style
Nice to have
• I would like it to be very clear, classy and as simple as possible
Should not have
• It needs to be neat not messy, symmetrical is better.

```html
<!DOCTYPE html>
<html lang="en">
<head>
<meta charset="utf-8">
<title>Healing the Addiction Cycle</title>
<link rel="stylesheet" href="https://fonts.googleapis.com/css2?family=Open+Sans:wght@400;600;700;800&display=swap">
<style>
:root{
  --stage:#8b8b8b;
  --paper:#ffffff;
  --navy:#1c2856;
  --blue:#2ba6e1;
  --blue-deep:#1a86c8;
  --arrow:#5bbbea;
  --ring:#e6e7ea;
}
*{box-sizing:border-box;margin:0;padding:0}
html,body{width:1200px;height:2687px;overflow:hidden}
body{background:var(--stage);font-family:"Open Sans",Arial,sans-serif;color:var(--navy);position:relative}
.slide{position:absolute;left:32px;width:1136px;background:var(--paper);border-radius:16px;overflow:hidden;box-shadow:0 2px 8px rgba(0,0,0,.25)}
.slide-1{top:27px;height:854px}
.slide-2{top:901px;height:851px}
.slide-3{top:1773px;height:883px}
.slide-header{position:absolute;left:0;top:0;width:100%;height:107px;background:linear-gradient(180deg,#8fd6f7 0%,var(--blue) 45%,var(--blue-deep) 100%);border-bottom-left-radius:40px 20px;border-bottom-right-radius:40px 20px;z-index:5}
.brand{position:absolute;left:26px;top:30px;display:flex;align-items:center;gap:12px;color:#fff;font-weight:600;font-size:26px;letter-spacing:-.3px}
.brand-dot{width:46px;height:46px;border-radius:50%;border:3px solid #fff}
.slide-title{position:absolute;left:300px;right:30px;top:0;height:107px;display:flex;align-items:center;justify-content:center;text-align:center;font-weight:800;color:var(--navy);font-size:38px;line-height:1.1}
.slide-2 .slide-title,.slide-3 .slide-title{font-size:33px}
.cycle{position:absolute;left:0;top:0;z-index:1}
.note{position:absolute;z-index:2;border:2px solid var(--navy);background:#fff;font-size:16px;line-height:1.28;padding:8px 12px;color:var(--navy)}
.note ul{list-style:none}
.note li::before{content:"\2022\00a0"}
.note li{margin-bottom:3px}
.note.spaced li{margin-bottom:16px}
.stage-node{position:absolute;z-index:3;border-radius:50%;background:radial-gradient(circle at 40% 30%,#8fdcfb 0%,var(--blue) 55%,var(--blue-deep) 100%);border:5px solid #fff;box-shadow:0 3px 8px rgba(0,0,0,.3);display:flex;align-items:center;justify-content:center;text-align:center;font-weight:800;color:var(--navy);font-size:21px;line-height:1.15;padding:16px}
.stage-node.small{font-size:16px;padding:14px}
.stage-node.tiny{font-size:13px;line-height:1.12;padding:20px}
.relief{position:absolute;z-index:4;left:430px;top:712px;padding:4px 18px;background:var(--blue);color:#fff;font-weight:800;font-size:21px;border-radius:10px;transform:rotate(14deg);box-shadow:0 2px 4px rgba(0,0,0,.25)}
.hub{position:absolute;z-index:0;left:351px;top:261px;width:412px;height:412px;border-radius:50%;background:radial-gradient(circle,#f4f4f5 60%,var(--ring) 100%);display:flex;align-items:center;justify-content:center}
.hub-core{width:330px;height:330px;border-radius:50%;background:#fff;box-shadow:0 0 14px rgba(0,0,0,.12);display:flex;align-items:center;justify-content:center;text-align:center;padding:34px;color:var(--blue);font-weight:800;font-size:22px;line-height:1.3}
.belief{position:absolute;z-index:4;border-radius:30px;background:radial-gradient(circle at 40% 30%,#a5e3fb,var(--blue));border:3px solid #fff;box-shadow:0 2px 6px rgba(0,0,0,.25);color:var(--navy);font-weight:700;font-size:17px;line-height:1.2;text-align:center;display:flex;align-items:center;justify-content:center;padding:6px 12px}
.studio{position:absolute;left:25px;bottom:22px;display:flex;align-items:center;gap:10px;color:var(--blue);font-weight:600;font-size:36px;letter-spacing:-.5px}
.studio-dot{width:16px;height:16px;border-radius:50%;background:var(--blue)}
.footnote{position:absolute;left:424px;top:846px;font-size:16px;color:var(--navy)}
</style>
</head>
<body>
<svg width="0" height="0" style="position:absolute">
  <defs>
    <marker id="head" viewBox="0 0 10 10" refX="5" refY="5" markerWidth="3.2" markerHeight="3.2" orient="auto">
      <path d="M0 0 L10 5 L0 10 z" fill="#5bbbea"/>
    </marker>
  </defs>
</svg>

<section class="slide slide-1">
  <header class="slide-header">
    <div class="brand"><span class="brand-dot"></span>Still Path Healing</div>
    <h1 class="slide-title">The Addiction Cycle Explained</h1>
  </header>
  <svg class="cycle" width="1136" height="854" fill="none" stroke="#5bbbea" stroke-width="12" stroke-linecap="round">
    <path d="M555 205 Q480 200 428 238" marker-end="url(#head)"/>
    <path d="M325 388 Q308 462 328 538" marker-end="url(#head)"/>
    <path d="M422 682 Q500 722 586 720" marker-end="url(#head)"/>
    <path d="M745 642 Q790 612 810 562" marker-end="url(#head)"/>
    <path d="M855 368 Q830 298 722 252" marker-end="url(#head)"/>
  </svg>
  <div class="note" style="left:32px;top:134px;width:235px;height:274px;padding-right:16px">Mental and emotional pain becomes physically unbearable and our unconscious desire to sooth or suppress it creates the craving/desire to overcome the pain through the addictive behavior</div>
  <div class="note" style="left:32px;top:510px;width:222px;height:224px">When can no longer hold back our desire/craving so we commit self abuse through addictive behaviour e.g. drugs, alcohol, food, gambling, exercise etc..</div>
  <div class="note" style="left:265px;top:751px;width:261px;height:85px">We experience a brief relief from emotion, mental and physical pain</div>
  <div class="note" style="left:720px;top:112px;width:343px;height:104px;padding-left:18px">Physical (ie: nausea, anxiety, depression) and mental reaction (ie: Negative self talk) to the emotional response</div>
  <div class="note" style="left:935px;top:370px;width:175px;height:185px">This is the emotional reaction to self judgment. This is often experienced on an unconscious level</div>
  <div class="note" style="left:768px;top:676px;width:295px;height:138px">We know judge ourselves for carrying out the addictive behavior: I'm not good enough, I'm a failure, I am weak. This process is often unconscious</div>

  <div class="stage-node small" style="left:555px;top:133px;width:164px;height:164px">Negative Thoughts, Physical Pain, Heavy emotions</div>
  <div class="stage-node" style="left:254px;top:209px;width:172px;height:172px">Desire/ Craving</div>
  <div class="stage-node" style="left:258px;top:546px;width:172px;height:172px">Act on the addiction</div>
  <div class="stage-node" style="left:594px;top:621px;width:172px;height:172px">Self Judgment</div>
  <div class="stage-node small" style="left:763px;top:370px;width:172px;height:172px">We experience Regret/ Guilt/Shame Sadness</div>
  <div class="relief">Relief</div>
  <div class="studio"><span class="studio-dot"></span>Calm Vessel</div>
</section>

<section class="slide slide-2">
  <header class="slide-header">
    <div class="brand"><span class="brand-dot"></span>Still Path Healing</div>
    <h1 class="slide-title">Healing The Addiction<br>Cycle with SPH</h1>
  </header>
  <div class="hub"><div class="hub-core">You don't need to worry that you've acted on the addiction-at all points in the cycle there is something you can do to heal yourself from it.</div></div>
  <svg class="cycle" width="1136" height="851" fill="none" stroke="#5bbbea" stroke-width="12" stroke-linecap="round">
    <path d="M570 195 Q480 195 434 240" marker-end="url(#head)"/>
    <path d="M330 412 Q310 482 330 548" marker-end="url(#head)"/>
    <path d="M425 692 Q500 736 584 732" marker-end="url(#head)"/>
    <path d="M750 640 Q800 600 815 556" marker-end="url(#head)"/>
    <path d="M855 368 Q835 290 742 250" marker-end="url(#head)"/>
  </svg>
  <div class="note spaced" style="left:57px;top:173px;width:219px;height:224px;padding-right:34px"><ul><li>What is the emotion I am experiencing?</li><li>Feel where it is in the body</li><li>Turn it up</li><li>Release It</li></ul></div>
  <div class="note" style="left:723px;top:110px;width:315px;height:130px;padding-left:22px"><ul><li>What is the emotion I am experiencing?</li><li>Feel where it is in the body</li><li>Turn it up</li><li>Release It</li></ul></div>
  <div class="note" style="left:931px;top:358px;width:179px;height:194px"><ul><li>What is the emotion I am experiencing?</li><li>Feel where it is in the body</li><li>Turn it up</li><li>Release It</li></ul></div>
  <div class="note" style="left:768px;top:671px;width:295px;height:143px">Practice forgiveness and compassion for self ie: I love you, I'm sorry, Please forgive me, Thank you</div>

  <div class="stage-node small" style="left:570px;top:115px;width:170px;height:170px">Physical and mental reaction to the emotional response</div>
  <div class="stage-node tiny" style="left:242px;top:209px;width:196px;height:196px">Desire to repress or deny compounded by the physical, mental and emotional pain responsible becomes unbearable</div>
  <div class="stage-node small" style="left:764px;top:369px;width:170px;height:170px">Emotional Reaction to self judgment</div>
  <div class="stage-node tiny" style="left:254px;top:552px;width:180px;height:180px">Commit self abuse through addictive behaviour e.g. drugs, alcohol, food, gambling, exercise etc..</div>
  <div class="stage-node" style="left:590px;top:616px;width:180px;height:180px">Self Judgment</div>
  <div class="studio"><span class="studio-dot"></span>Calm Vessel</div>
</section>

<section class="slide slide-3">
  <header class="slide-header">
    <div class="brand"><span class="brand-dot"></span>Still Path Healing</div>
    <h1 class="slide-title">SPH Treatment of the Addiction Cycle<br>-Practitioners Guide</h1>
  </header>
  <svg class="cycle" width="1136" height="883" fill="none" stroke="#5bbbea" stroke-width="12" stroke-linecap="round">
    <path d="M570 240 Q480 235 432 272" marker-end="url(#head)"/>
    <path d="M330 412 Q314 500 334 578" marker-end="url(#head)"/>
    <path d="M430 708 Q510 752 584 748" marker-end="url(#head)"/>
    <path d="M752 652 Q800 622 815 600" marker-end="url(#head)"/>
    <path d="M855 414 Q835 330 740 276" marker-end="url(#head)"/>
  </svg>
  <div class="note" style="left:741px;top:151px;width:292px;height:58px;padding-left:16px"><ul><li>Complete the SPH Emotional Release process</li></ul></div>
  <div class="note" style="left:32px;top:196px;width:204px;height:94px"><ul><li>Complete the SPH Emotional Release Process</li></ul></div>
  <div class="note" style="left:32px;top:298px;width:204px;height:376px;border-bottom-right-radius:40px;font-size:15px;line-height:1.25">You don't need to worry that you've acted on the addiction, at all points in the cycle there is something you can do to heal yourself from it. Addiction Sits at the level of desire/ craving and ust be measured before and after. You CAN NOT release addiction without releasing shame.</div>
  <div class="note" style="left:931px;top:397px;width:179px;height:112px"><ul><li>Complete the SPH Emotional release process</li></ul></div>
  <div class="note" style="left:778px;top:690px;width:200px;height:132px;padding-left:16px"><ul><li>Complete the SPH Emotional release process</li><li>ho'oponopono</li><li>Inner child</li></ul></div>

  <div class="stage-node small" style="left:573px;top:153px;width:164px;height:164px">Negative Thoughts, Physical Pain, Heavy emotions</div>
  <div class="stage-node" style="left:254px;top:235px;width:172px;height:172px">Desire/ Craving</div>
  <div class="stage-node" style="left:258px;top:584px;width:172px;height:172px">Substance Abuse</div>
  <div class="stage-node" style="left:590px;top:639px;width:180px;height:180px">Judgment</div>
  <div class="stage-node" style="left:763px;top:418px;width:172px;height:172px">Regret/ Guilt/ Shame</div>
  <div class="belief" style="left:363px;top:373px;width:170px;height:64px">I am a slave to my desires</div>
  <div class="belief" style="left:494px;top:556px;width:230px;height:120px">I am a slave to my desires I'm not good enough, I'm a failure I am weak</div>
  <div class="footnote">For limiting belief diagnosis use beliefs that sit under the level of desire</div>
  <div class="studio"><span class="studio-dot"></span>Calm Vessel</div>
</section>
</body>
</html>
```